Design the New 3D Printing Database - MeshVaultly.net

We’re hiring a designer to create a modern, intuitive, and scalable frontend design for MeshVaultly.net — a search engine and aggregator for free 3D printable files (STL files).

The site will not host files, but will crawl and display listings from other 3D file platforms like Cubomark, Layerhaven, and OurTinyWorkshop. We need a design that looks clean, tech-forward, and makes it easy for users to browse, search, and explore curated 3D print models.

Project Goals
• Help users search, filter, and browse STL files from various sources
• Present file listings in a clean and organized card-style layout
• Include strong category navigation, tag filtering, and search UX
• Allow for expansion — community features, user accounts, ads, etc.
• Be ready for handoff to developers

Pages & Components to Design

1. Homepage
• Featured models / Trending prints
• Search bar with predictive text
• Top categories (e.g., Tools, Toys, Miniatures, Cosplay)
• Optional: promo ad slot or “Featured Site of the Week”

2. Search Results Page
• Search bar at top
• Grid or list view of STL listings
• Filters on sidebar (category, tag, source site, popularity)
• Sort options (Newest, Most Viewed, Top Rated)

3. Individual File Listing Page
• Model thumbnail (placeholder for external image)
• Title, description, tags
• Source website badge/logo
• Button: “View on [Source Site]”
• Optional: 3D viewer embed (room for iframe or canvas)

4. Category Pages
• Header with category name and short description
• Grid of listings in that category

5. About / FAQ / Submit a File
• Basic static content page layout
• Contact form or submission form mockup

6. Admin Preview (Optional)
• Just 1-2 styled screens for how backend editing might look (not functional)

Design Requirements
• Responsive (desktop, tablet, mobile)
• Clean, modern UI (think: Web3 simplicity, Zundero-level UX)
• Easy-to-read typography and smart use of whitespace
• Icons or badges for source platforms (e.g., Cubomark, Layerhaven)
• Room for advertising placements (sidebar, inline, or homepage)

Style Inspiration
• Hero inspiration: PolyScout.net — but cleaner
• Other ideas: Brenvo Commons, Plixtrove
• Optional: light/dark mode theme toggle

Deliverables
• Complete desktop and mobile Figma designs
• Style guide (colors, fonts, components)
• Assets and UI kit for development handoff
• Optionally, clickable prototype for demonstration

3D Printing Enthusiasts

3D Printing, Design, Engineering

5+ page

Sans Serif

```html
<!DOCTYPE html>
<html lang="en">
<head>
<meta charset="utf-8">
<title>MeshVaultly.net — Free 3D Printable Models</title>
<link rel="stylesheet" href="https://fonts.googleapis.com/css2?family=Lexend:wght@500;600;700&family=Outfit:wght@400;500;600&display=swap">
<style>
:root{
  --brand:#5641df;
  --brand-dark:#4532c9;
  --brand-soft:#eeebfd;
  --ink:#1e1d2b;
  --text:#2c2b38;
  --muted:#6c6b78;
  --line:#e3e2ea;
  --card-shadow:0 10px 30px rgba(40,30,90,.08);
  --white:#fff;
}
*{box-sizing:border-box;margin:0;padding:0}
html,body{width:1200px;height:2621px;overflow:hidden}
body{position:relative;background:var(--white);font-family:"Outfit",sans-serif;color:var(--text)}
.abs{position:absolute}
h1,h2,h3,.logo{font-family:"Lexend",sans-serif;color:var(--ink)}

/* header */
.logo{font-weight:600;font-size:18px}
.site-header .logo{left:92px;top:24px}
.main-nav{left:434px;top:28px;display:flex;gap:30px;font-size:13px;align-items:center}
.main-nav svg{width:16px;height:16px}
.header-search{left:825px;top:20px;width:200px;height:35px;border:1px solid var(--line);border-radius:18px;font-size:12px;color:#9a99a5;padding:10px 18px}
.header-search svg{position:absolute;right:14px;top:11px;width:12px;height:12px}
.theme-toggle{left:1032px;top:20px;width:55px;height:35px;border-radius:18px;background:var(--brand)}
.theme-toggle span{position:absolute;left:4px;top:4px;width:27px;height:27px;border-radius:50%;background:#fff}
.theme-toggle svg{position:absolute;left:9px;top:9px;width:17px;height:17px}

/* hero */
.hero-title{left:92px;top:204px;font-size:31px;font-weight:600;line-height:39px;letter-spacing:-.2px}
.hero-title em{font-style:normal;color:var(--brand)}
.hero-lead{left:91px;top:296px;width:430px;font-size:12px;line-height:17px}
.hero-search{left:97px;top:345px;width:448px;height:36px;border:1px solid var(--line);border-radius:18px;font-size:12px;color:#8b8a96;padding:10px 14px}
.hero-search button{position:absolute;right:-1px;top:-1px;width:125px;height:36px;border:0;border-radius:18px;background:var(--brand);color:#fff;font:500 12px "Outfit",sans-serif;display:flex;align-items:center;justify-content:center;gap:8px}
.quick-tags{left:97px;top:388px;display:flex;gap:6px}
.pill{border:1px solid var(--line);border-radius:18px;font-size:12px;padding:9px 18px;color:#5c5b68}
.shot{position:absolute;border-radius:2px}

/* categories */
.section-title{width:1200px;text-align:center;font-weight:600;font-size:28px}
.category-row{left:252px;top:654px;display:flex;gap:7px}
.category{width:78px;text-align:center;font-size:12px;color:var(--text)}
.category .disc{width:78px;height:78px;border-radius:50%;border:1px solid var(--line);padding:6px;margin-bottom:9px}
.category .disc i{display:block;width:100%;height:100%;border-radius:50%}
.btn{display:inline-flex;align-items:center;justify-content:center;border-radius:18px;font-size:12px;font-weight:500;height:35px}
.btn-primary{background:var(--brand);color:#fff}
.btn-soft{background:var(--brand-soft);color:var(--brand)}

/* trending */
.subtitle{width:1200px;text-align:center;font-size:12px}
.model-card{position:absolute;width:290px;height:361px;border-radius:16px;background:#fff;box-shadow:var(--card-shadow);overflow:hidden}
.model-card .thumb{height:200px}
.model-card .body{position:absolute;top:193px;left:0;right:0;bottom:0;background:#fff;border-radius:16px 16px 0 0;padding:26px 31px}
.model-card h3{font-size:16.5px;font-weight:600;margin-bottom:4px}
.model-card .src{font-size:11.5px}
.model-card .src b{font-weight:600}
.tags{display:flex;gap:4px;margin:9px 0 13px}
.tags span{border:1px solid var(--line);border-radius:12px;font-size:8.5px;padding:6px 15px;color:#6c6b78}
.model-card .btn{height:30px;padding:0 19px;font-weight:400}

/* community */
.divider{left:589px;top:1802px;width:1px;height:254px;background:#cfcdd8}
.cta{width:420px;text-align:center}
.cta h2{font-size:25px;font-weight:600;line-height:32px;margin-bottom:12px}
.cta p{font-size:12px;line-height:17px;margin-bottom:17px}
.cta .actions{display:flex;justify-content:center;align-items:center;gap:11px;font-size:12px}
.cta .btn{padding:0 20px}

/* featured */
.featured{left:0;top:2123px;width:1200px;height:240px;border-radius:64px 64px 0 0;background:
 radial-gradient(circle at 830px 150px,#3b27b8 0,rgba(59,39,184,0) 90px),
 radial-gradient(circle at 1000px 60px,#6c58ee 0,rgba(108,88,238,0) 160px),
 linear-gradient(90deg,#5a46e0,#5340d6)}
.featured h2{position:absolute;left:115px;top:62px;color:#fff;font-size:29px;font-weight:600}
.featured p{position:absolute;left:115px;top:102px;color:#fff;font-size:12px}
.featured .btn{position:absolute;left:902px;top:72px;width:157px;background:#fff;color:var(--ink);font-weight:400}

/* footer */
.site-footer{left:0;top:2306px;width:1200px;height:315px;background:#fff;border-radius:48px 48px 0 0}
.site-footer .logo{position:absolute;left:118px;top:90px;font-size:28px}
.tagline{position:absolute;left:154px;top:130px;font-size:12px}
.footer-nav{position:absolute;right:150px;top:88px;display:flex;gap:24px;font-size:12.5px}
.social{position:absolute;right:150px;top:124px;display:flex;gap:18px;font-size:11px;color:var(--ink);font-weight:500}
.footer-rule{position:absolute;left:92px;top:216px;width:995px;height:1px;background:var(--line)}
.copyright{position:absolute;left:0;top:234px;width:1200px;text-align:center;font-size:12px}
.to-top{position:absolute;left:1099px;top:200px;width:33px;height:33px;border-radius:50%;background:var(--brand)}
.to-top svg{position:absolute;left:11px;top:11px}
</style>
</head>
<body>

<header class="site-header">
  <div class="abs logo">MeshVaultly.net</div>
  <nav class="abs main-nav">
    <svg viewBox="0 0 16 16" fill="none" stroke="#5641df" stroke-width="1.4"><path d="M2 7.5 8 2.5l6 5V14H10v-4H6v4H2z"/></svg>
    <span>Categories</span><span>Popular</span><span>Submit a File</span><span>About</span>
  </nav>
  <div class="abs header-search">Search here...
    <svg viewBox="0 0 12 12" fill="none" stroke="#1e1d2b" stroke-width="1.6"><circle cx="5" cy="5" r="3.8"/><path d="m8 8 3 3"/></svg>
  </div>
  <div class="abs theme-toggle"><span></span>
    <svg viewBox="0 0 18 18" fill="#1e1d2b" stroke="#1e1d2b" stroke-width="1.5"><circle cx="9" cy="9" r="3.6"/><path d="M9 1v2M9 15v2M1 9h2M15 9h2M3.3 3.3l1.4 1.4M13.3 13.3l1.4 1.4M3.3 14.7l1.4-1.4M13.3 4.7l1.4-1.4"/></svg>
  </div>
</header>

<section class="hero">
  <h1 class="abs hero-title">Discover &amp; Search Thousands of<br>Free <em>3D</em> Printable Models</h1>
  <p class="abs hero-lead">Explore curated STL files from top platforms like Cubomark, Layerhaven, and OurTinyWorkshop — all in one place.</p>
  <div class="abs hero-search">Search models, categories, tags...
    <button><svg width="12" height="12" viewBox="0 0 12 12" fill="none" stroke="#fff" stroke-width="1.6"><circle cx="5" cy="5" r="3.8"/><path d="m8 8 3 3"/></svg>Search</button>
  </div>
  <div class="abs quick-tags">
    <span class="pill">Miniatures</span><span class="pill">Tools</span><span class="pill">Cosplay</span><span class="pill">Toys</span><span class="pill">Figurines</span>
  </div>

  <div class="shot" style="left:756px;top:146px;width:111px;height:62px;background:linear-gradient(135deg,#a9c9e3,#7fb0d8)" role="img" aria-label="Printed blue truck with yellow trailer"></div>
  <div class="shot" style="left:877px;top:100px;width:193px;height:166px;background:linear-gradient(135deg,#dcdcde,#c9c3b8)" role="img" aria-label="Orange printed roadster car"></div>
  <div class="shot" style="left:1080px;top:171px;width:92px;height:167px;background:linear-gradient(180deg,#1a1a1c,#0c0c0d)" role="img" aria-label="White printed rocket on dark background"></div>
  <div class="shot" style="left:674px;top:218px;width:193px;height:130px;background:linear-gradient(135deg,#d6d6d4,#b8b59f)" role="img" aria-label="Olive green printed tank model"></div>
  <div class="shot" style="left:877px;top:276px;width:92px;height:148px;background:linear-gradient(180deg,#141416,#2a2a2e)" role="img" aria-label="Printed space shuttle on launch stand"></div>
  <div class="shot" style="left:979px;top:276px;width:91px;height:62px;background:linear-gradient(135deg,#ededec,#d9c7b5)" role="img" aria-label="Small printed cottage"></div>
  <div class="shot" style="left:674px;top:358px;width:75px;height:76px;background:linear-gradient(135deg,#1c1412,#3a2e2a)" role="img" aria-label="Twisted printed lamp shade"></div>
  <div class="shot" style="left:760px;top:358px;width:107px;height:107px;background:linear-gradient(135deg,#dde3e8,#a7c9e6)" role="img" aria-label="Blue articulated toy robot"></div>
  <div class="shot" style="left:877px;top:434px;width:92px;height:92px;background:linear-gradient(135deg,#ecebe9,#dcd6cc)" role="img" aria-label="Textured printed vase"></div>
  <div class="shot" style="left:979px;top:347px;width:221px;height:198px;background:linear-gradient(135deg,#e4e4e4,#d8d2bf)" role="img" aria-label="Yellow printed excavator"></div>
</section>

<section class="categories">
  <h2 class="abs section-title" style="top:594px">Explore by Category</h2>
  <div class="abs category-row">
    <div class="category"><div class="disc"><i style="background:radial-gradient(#fde0a3,#fdf2dc)"></i></div>Toys</div>
    <div class="category" style="margin-left:8px"><div class="disc"><i style="background:radial-gradient(#dcd3f4,#f1edfb)"></i></div>Miniatures</div>
    <div class="category"><div class="disc"><i style="background:radial-gradient(#f6cd7e,#c9e6f6)"></i></div>Tools</div>
    <div class="category"><div class="disc"><i style="background:radial-gradient(#8a80e6,#d5d8ef)"></i></div>Cosplay</div>
    <div class="category" style="margin-left:8px"><div class="disc"><i style="background:radial-gradient(#f3d38c,#fbf1de)"></i></div>Educational</div>
    <div class="category"><div class="disc"><i style="background:radial-gradient(#f2a9b6,#fde3d3)"></i></div>Fantasy</div>
    <div class="category"><div class="disc"><i style="background:radial-gradient(#f3a29a,#fde0dc)"></i></div>Art</div>
    <div class="category" style="margin-left:8px"><div class="disc"><i style="background:radial-gradient(#d9d4f3,#efedfb)"></i></div>Gadgets</div>
  </div>
  <a class="abs btn btn-primary" style="left:511px;top:782px;width:158px">View All Categories</a>
</section>

<section class="trending">
  <h2 class="abs section-title" style="top:888px;font-size:30px">Trending 3D Models</h2>
  <p class="abs subtitle" style="top:933px">Updated daily — check out what’s hot in the 3D printing community.</p>

  <article class="model-card" style="left:145px;top:980px">
    <div class="thumb" role="img" aria-label="Purple dragon miniature" style="background:linear-gradient(135deg,#ecebf0,#d4d3da)"></div>
    <div class="body"><h3>Posable Dragon Miniature</h3><p class="src"><b>Source</b>: Layerhaven</p>
      <div class="tags"><span>Miniature</span><span>Fantasy</span><span>Articulated</span></div>
      <a class="btn btn-soft">View on Layerhaven</a></div>
  </article>
  <article class="model-card" style="left:444px;top:980px">
    <div class="thumb" role="img" aria-label="Blue printed wrench on grid" style="background:linear-gradient(180deg,#b4b4b8,#d7d7da)"></div>
    <div class="body"><h3>Adjustable Wrench Tool</h3><p class="src"><b>Source</b>: Cubomark</p>
      <div class="tags"><span>Workshop</span><span>Tool</span></div>
      <a class="btn btn-soft" style="padding:0 16px">View on Cubomark</a></div>
  </article>
  <article class="model-card" style="left:743px;top:980px">
    <div class="thumb" role="img" aria-label="White cosplay helmet" style="background:linear-gradient(135deg,#8d8d8f,#a8a8aa)"></div>
    <div class="body"><h3>Star Warrior Cosplay Helmet</h3><p class="src"><b>Source</b>: Layerhaven</p>
      <div class="tags"><span>Cosplay</span><span>Helmet</span></div>
      <a class="btn btn-soft">View on OurTinyWorkshop</a></div>
  </article>

  <article class="model-card" style="left:145px;top:1370px">
    <div class="thumb" role="img" aria-label="Yellow robotic arm with statue" style="background:linear-gradient(135deg,#f4f4f2,#e6e3c8)"></div>
    <div class="body"><h3>Articulated Desk Robot</h3><p class="src"><b>Source</b>: Cubomark</p>
      <div class="tags"><span>Miniature</span><span>Fantasy</span><span>Articulated</span></div>
      <a class="btn btn-soft" style="padding:0 16px">View on Cubomark</a></div>
  </article>
  <article class="model-card" style="left:444px;top:1370px">
    <div class="thumb" role="img" aria-label="White and black geometric vases" style="background:linear-gradient(135deg,#e9e9e9,#cfcfcf)"></div>
    <div class="body"><h3>Modern Geometric Vase Set</h3><p class="src"><b>Source</b>: OurTinyWorkshop</p>
      <div class="tags"><span>Workshop</span><span>Tool</span></div>
      <a class="btn btn-soft">View on OurTinyWorkshop</a></div>
  </article>
  <article class="model-card" style="left:743px;top:1370px">
    <div class="thumb" role="img" aria-label="White wall mount holder" style="background:linear-gradient(135deg,#f0f0f0,#e2e2e2)"></div>
    <div class="body"><h3>Universal Wall Mount Holder</h3><p class="src"><b>Source</b>: Layerhaven</p>
      <div class="tags"><span>Cosplay</span><span>Helmet</span></div>
      <a class="btn btn-soft">View on Layerhaven</a></div>
  </article>
</section>

<section class="community">
  <div class="abs divider"></div>
  <div class="abs cta" style="left:129px;top:1846px">
    <h2>MeshVaultly Community<br>Coming Soon!</h2>
    <p>Soon you’ll be able to save favorites, rate models,<br>and share your collections. Stay tuned.</p>
    <div class="actions"><a class="btn btn-primary">Join Waitlist</a>OR<a class="btn btn-soft">Get Notified</a></div>
  </div>
  <div class="abs cta" style="left:643px;top:1846px">
    <h2>Have a Great Model<br>to Share?</h2>
    <p>Submit a file link to share with the community. We’ll review<br>and add it if it fits our curation standards.</p>
    <div class="actions"><a class="btn btn-primary">Submit a File</a></div>
  </div>
</section>

<section class="abs featured" role="img" aria-label="Featured platform banner with floating geometric shapes">
  <h2>Featured Source Platform</h2>
  <p>This week we’re highlighting [Layerhaven.com], a go-to platform for high-quality STL files.</p>
  <a class="btn">Explore Layerhaven.com</a>
</section>

<footer class="abs site-footer">
  <div class="logo">MeshVaultly.net</div>
  <p class="tagline">The smarter way to search STL files.</p>
  <nav class="footer-nav"><span>Home</span><span>Categories</span><span>Popular</span><span>Submit a File</span><span>About</span><span>FAQ</span><span>Contact</span></nav>
  <div class="social"><span>Boardly</span><span>Quipster</span><span>Workloop</span><span>Snapgrid</span></div>
  <div class="footer-rule"></div>
  <a class="to-top"><svg width="11" height="11" viewBox="0 0 11 11" fill="none" stroke="#fff" stroke-width="1.6"><path d="M2.5 7 5.5 4l3 3"/></svg></a>
  <p class="copyright">© 2025 MeshVaultly.net — Aggregating the 3D printing world.</p>
</footer>

</body>
</html>
```